Cow.ThankYou

I want to combine the attached "Thank you Come Again billboard" with a cow or multiple cows standing around or laying next to the cow. The teepee etc can be eliminated from the background. It is to be used as a wall graphic in an ice cream/popsicle shop. I would like it if there is a way to incorporate my logo (which was done thru you) and if there is a way to make it instagramable so that people will take their picture next to the cows - hence the need for the Frostnook logo. I have attached a file of the "Thanks. Come Again" image and a couple cow ones to give an idea - the images don't have to be used if the designer finds better images - mostly I just want it to be a black and white cow with personality. I have also included the file that shows the dimensions of the wall area to be covered so the image can be sized appropriately.Lastly I have attached my logo.

```html
<!DOCTYPE html>
<html lang="en">
<head>
<meta charset="utf-8">
<title>Thanks Come Again – Frostnook wall graphic</title>
<link rel="stylesheet" href="https://fonts.googleapis.com/css2?family=Anton&family=Sansita:ital,wght@1,800&display=swap">
<style>
  :root {
    --ink: #2b2b2a;
    --wall-light: #fbfbfb;
    --wall-mid: #e9e9e9;
    --wall-edge: #d6d6d6;
    --cow-light: #ece8e4;
    --cow-dark: #2a2a2a;
  }
  html, body {
    margin: 0;
    padding: 0;
    width: 1200px;
    height: 858px;
    overflow: hidden;
    background: var(--wall-mid);
  }
  .wall-graphic {
    display: block;
    width: 1200px;
    height: 858px;
  }
  .headline-thanks,
  .headline-again {
    font-family: "Anton", "Impact", sans-serif;
    fill: var(--ink);
  }
  .headline-come {
    font-family: "Sansita", "Arial Black", sans-serif;
    font-style: italic;
    font-weight: 800;
    fill: var(--ink);
  }
  .brand-name {
    font-family: "Anton", "Impact", sans-serif;
    fill: var(--ink);
    font-size: 40px;
    letter-spacing: 1px;
  }
</style>
</head>
<body>
<svg class="wall-graphic" viewBox="0 0 1200 858" xmlns="http://www.w3.org/2000/svg">
  <defs>
    <radialGradient id="wall-tone" cx="0.5" cy="0.5" r="0.75">
      <stop offset="0" stop-color="var(--wall-light)"/>
      <stop offset="0.6" stop-color="var(--wall-mid)"/>
      <stop offset="1" stop-color="var(--wall-edge)"/>
    </radialGradient>
    <linearGradient id="cow-tone" x1="0" y1="0" x2="1" y2="1">
      <stop offset="0" stop-color="var(--cow-light)"/>
      <stop offset="0.45" stop-color="var(--cow-dark)"/>
      <stop offset="1" stop-color="var(--cow-light)"/>
    </linearGradient>
  </defs>

  <rect class="wall-background" x="0" y="0" width="1200" height="858" fill="url(#wall-tone)"/>

  <rect class="cow-photo" role="img" aria-label="Photo of a black and white Holstein cow standing and looking toward the viewer"
        x="864" y="90" width="320" height="514" rx="40" fill="url(#cow-tone)" opacity="0.85"/>

  <text class="brand-name" x="936" y="72" textLength="200" lengthAdjust="spacingAndGlyphs">Frostnook</text>

  <text class="headline-thanks" x="240" y="328" font-size="338"
        textLength="640" lengthAdjust="spacingAndGlyphs">THANKS</text>
  <text class="headline-come" x="56" y="578" font-size="250"
        textLength="380" lengthAdjust="spacingAndGlyphs">Come</text>
  <text class="headline-again" x="468" y="584" font-size="240"
        textLength="568" lengthAdjust="spacingAndGlyphs">AGAIN</text>
</svg>
</body>
</html>
```